QRT-LM R-Value Adjustment Paper

This is a technical paper needing professional layout that is compatible with our current style guidelines; it will be used in digital and print media. It has numerous tables and graphs.

We have attached a report "QRT Cladding Dossier" issued to our company under Pellworth Certifiers graphic design guidelines. While this does NOT reflect our style branding, it does represent the 'technical' presentation we are looking for.

To view our typical company design/style please see our website at www.qrtfabric.org. Our primary RGB colors are: (187,140,9); (94,47,29); (94,138,164); and (164,167,15). Secondary RGB colors are (249,162,28) and (218,210,208). Our title/header font is DIN Next LT Pro and our copy font is Calibri 10.5 pt. We can deviate from the font specification if beneficial.

The attached file, "QRT-LM Rvalue Adj Factor" is a partial representation of the full document that will need design services. For the concepts we would like to see a cover/title page, a text/copy page and a sample of data graphic treatments.Once we have agreed upon a design concept we will determine full costs to complete the project.

Target Market(s)

Building and construction professionals, architects, building code officials

Font styles to use
Other font styles liked:
• DIN Next LT Pro

Requirements
Must have
• Design elements that help make the information easy to read and use.
Nice to have
• Right amount of white space.

```html
<!DOCTYPE html>
<html lang="en">
<head>
<meta charset="utf-8">
<title>QRT-LM R-Value Adjustment Paper – Page 2</title>
<link href="https://fonts.googleapis.com/css2?family=Roboto+Condensed:wght@700&family=Carlito:ital,wght@0,400;0,700;1,400&display=swap" rel="stylesheet">
<style>
  :root {
    --accent-green: #9cc31b;
    --formula-green: #b3d236;
    --marker-gold: #b8980c;
    --ink: #1a1a1a;
    --grid: #c8c8c8;
    --eps-blue: #4f9ec1;
    --xps-orange: #f7941d;
    --white: #ffffff;
  }
  html, body { margin: 0; padding: 0; overflow: hidden; }
  body { width: 855px; height: 1200px; background: var(--white); color: var(--ink); font-family: "Carlito", "Calibri", sans-serif; }
  .page { position: relative; width: 855px; height: 1200px; overflow: hidden; }

  .section-head { position: absolute; left: 25px; width: 803px; height: 56px; }
  .section-marker {
    position: absolute; left: 52px; top: 19px; width: 12px; height: 12px;
    background: var(--marker-gold);
  }
  .section-title {
    position: absolute; left: 73px; top: 4px; margin: 0;
    font: 700 31px/40px "Roboto Condensed", sans-serif; color: #111; letter-spacing: -0.3px;
  }
  .section-rule { position: absolute; left: 73px; right: 0; top: 49px; height: 4px; background: var(--accent-green); }

  .chart { position: absolute; left: 0; top: 0; }
  .chart text { font-family: "Carlito", sans-serif; font-size: 14px; fill: #222; }
  .figure-caption { position: absolute; left: 73px; top: 549px; margin: 0; font-size: 14.5px; font-style: italic; white-space: nowrap; }

  .body-copy { position: absolute; left: 25px; width: 810px; margin: 0; font-size: 14.5px; line-height: 17.6px; white-space: nowrap; }
  .formula {
    position: absolute; left: 25px; top: 1013px; width: 262px; height: 22px; padding-left: 8px;
    background: var(--formula-green); font: 700 14px/22px "Carlito", sans-serif;
  }
  .definitions { position: absolute; left: 25px; top: 1043px; margin: 0; font-size: 14.5px; line-height: 17.6px; white-space: nowrap; }
  .definitions b { font-weight: 700; }
  .page-number {
    position: absolute; left: 784px; top: 1124px; width: 44px; height: 44px;
    background: var(--accent-green); color: var(--white); border-radius: 0 0 0 8px;
    font: 700 30px/44px "Roboto Condensed", sans-serif; text-align: center;
  }
</style>
</head>
<body>
<div class="page">

  <header class="section-head" style="top:20px">
    <div class="section-marker"></div>
    <h2 class="section-title">Moisture</h2>
    <div class="section-rule"></div>
  </header>

  <svg class="chart" width="855" height="540" viewBox="0 0 855 540" role="img" aria-label="Line chart of R-value loss versus moisture volume percent for EPS and XPS">
    <g stroke="var(--grid)" stroke-width="1">
      <line x1="73" y1="105" x2="688" y2="105"/>
      <line x1="73" y1="176.6" x2="688" y2="176.6"/>
      <line x1="73" y1="248.2" x2="688" y2="248.2"/>
      <line x1="73" y1="319.8" x2="688" y2="319.8"/>
      <line x1="73" y1="391.4" x2="688" y2="391.4"/>
      <line x1="73" y1="463" x2="688" y2="463"/>
      <line x1="73" y1="105" x2="73" y2="463"/>
      <line x1="161" y1="105" x2="161" y2="463"/>
      <line x1="249" y1="105" x2="249" y2="463"/>
      <line x1="337" y1="105" x2="337" y2="463"/>
      <line x1="424" y1="105" x2="424" y2="463"/>
      <line x1="512" y1="105" x2="512" y2="463"/>
      <line x1="600" y1="105" x2="600" y2="463"/>
      <line x1="688" y1="105" x2="688" y2="463"/>
    </g>
    <g text-anchor="start">
      <text x="30" y="110">25</text>
      <text x="30" y="182">20</text>
      <text x="30" y="253">15</text>
      <text x="30" y="325">10</text>
      <text x="36" y="396">5</text>
      <text x="36" y="468">0</text>
    </g>
    <g text-anchor="middle">
      <text x="73" y="496">0</text><text x="161" y="496">1</text><text x="249" y="496">2</text>
      <text x="337" y="496">3</text><text x="424" y="496">4</text><text x="512" y="496">5</text>
      <text x="600" y="496">6</text><text x="688" y="496">7</text>
      <text x="372" y="524">Moisture, Vol%</text>
    </g>
    <polyline fill="none" stroke="var(--eps-blue)" stroke-width="4" points="73,463 161,404.3 249,352.7 337,299.8 424,249.6 512,198 600,156.6"/>
    <g fill="var(--eps-blue)">
      <circle cx="73" cy="463" r="6.5"/><circle cx="161" cy="404.3" r="6.5"/><circle cx="249" cy="352.7" r="6.5"/>
      <circle cx="337" cy="299.8" r="6.5"/><circle cx="424" cy="249.6" r="6.5"/><circle cx="512" cy="198" r="6.5"/>
      <circle cx="600" cy="156.6" r="6.5"/>
    </g>
    <polyline fill="none" stroke="var(--xps-orange)" stroke-width="4" points="73,463 161,427.2 249,391.4 337,355.6 424,319.8 512,291.2 600,264"/>
    <g fill="var(--xps-orange)">
      <circle cx="73" cy="463" r="6.5"/><circle cx="161" cy="427.2" r="6.5"/><circle cx="249" cy="391.4" r="6.5"/>
      <circle cx="337" cy="355.6" r="6.5"/><circle cx="424" cy="319.8" r="6.5"/><circle cx="512" cy="291.2" r="6.5"/>
      <circle cx="600" cy="264" r="6.5"/>
    </g>
    <line x1="710" y1="258" x2="778" y2="258" stroke="var(--eps-blue)" stroke-width="4"/>
    <circle cx="744" cy="258" r="6.5" fill="var(--eps-blue)"/>
    <text x="791" y="263">EPS</text>
    <line x1="710" y1="309" x2="778" y2="309" stroke="var(--xps-orange)" stroke-width="4"/>
    <circle cx="744" cy="309" r="6.5" fill="var(--xps-orange)"/>
    <text x="791" y="314">XPS</text>
  </svg>

  <p class="figure-caption">Figure 4.&nbsp; Loss of R-value by Polystyrene Foam Insulation Due to the Absorption of moisture (ISO, 2007)</p>

  <header class="section-head" style="top:620px">
    <div class="section-marker"></div>
    <h2 class="section-title">Effective R-value</h2>
    <div class="section-rule"></div>
  </header>

  <p class="body-copy" style="top:688px">The discussion on temperature, moisture, and aging demonstrated that R-value is affected by each of these considerations.&nbsp; A method-<br>ology that includes all three considerations can be used to determine the effective R-value under specific building conditions.</p>

  <header class="section-head" style="top:768px">
    <div class="section-marker"></div>
    <h2 class="section-title">Effective R-value Determination</h2>
    <div class="section-rule"></div>
  </header>

  <p class="body-copy" style="top:838px">The adjustment of the R-value from ideal laboratory conditions to the conditions in building applications is straightforward.&nbsp; The Ef-<br>fective R-value determination discussed herein is analogous to a thermal conductivity adjustment method recognized in international<br>standard ISO 10456 (ISO, 2007).<br>The R-value determined in the laboratory (RLAB) by following the FTC R-value Rule is multiplied by three adjustment factors to deter-<br>mine the effective R-value (REFFECTIVE).&nbsp; There is an adjustment factor for moisture (FH20) where this value is a number less than or<br>equal to one, since moisture will have a negative impact on the R-value.&nbsp; There is an adjustment factor for temperature (FTEMP) where<br>this value may be less than or greater than one depending on the change in performance relative to the R-value determined at the<br>mean temperature of 75°F.&nbsp; There is an adjustment factor for aging (FAGE)where this value is a number equal to or less than one since<br>the R-value will decrease over time for some products due to the loss of captive blowing agents.</p>

  <div class="formula">REFFECTIVE = RLAB x FTEMP x FAGE x FH20</div>

  <p class="definitions">where:<br>
    <b>REFFECTIVE</b> = effective R-value under the specific conditions considered<br>
    <b>RLAB</b> = R-value determined under standard laboratory conditions at 75 °F mean temperature in accordance with the FTC R-value Rule<br>
    <b>FTEMP</b> = adjustment factor for temperature<br>
    <b>FAGE</b> = adjustment factor for a product that is 50 years old<br>
    <b>FH20</b> = adjustment factor for moisture based on application</p>

  <div class="page-number">2</div>
</div>
</body>
</html>
```